Elegant and modern body scrub for organic junkies

I need a package design for my new company based out of Austin, Texas. We are focused on cruelty free and all natural and organic products. Our deign needs to be able to have the information we require on it, while still appearing very clean and captivating. Our initial product is a clear skin body scrub, intended for people with problematic skin. Our target market is women and we want to show elegance, without appearing "high end."
Updates

Reason: I want to allot more time for certain designers to submit edits. Last minute proposals have been appealing

Target Market(s)

Women. Organic and holistic minded. Natural beauty lovers.

Industry/Entity Type

Skin Care Product

Font styles to use
Script
Other font styles liked:
• AmericanTypewriter, Beautifulflaws, courier, caviarDreams-bold

Colors
000000
ffc214
ffffff
fece3e
fbee3e

Requirements
Must have
• Must be designed in Adobe Illustrator.
• The photo titled “structure for oz and grams” -That needs to be included at the bottom of 1B. I like the horizontal and vertical bar that separate the two. I want that.
• Color Inspiration - The photo titled “vorna color inspiration” and “color combo inspiration” are the colors I want. BLACK, GOLD, WHITE. I want the label background black and the writing in white with some gold somewhere on it. My logo is going to be a golden elephant.
• The photos titled “I like how clean this looks” and “I also like how clean this looks” - I want 1B to look super clean. I don’t want a lot of information in this box. I want simple and clean. This is where the logo and brand name will go.
• Logo - A golden elephant. I want it to be gold and geometric. There can be dimension like this elephant example on the left of the 1B description. I want the trunk to be facing to the left and the trunk needs to be raised overhead and touching the animal's forehead.
• The photo titled “sideways writing and silver rim” - I want 1C to be written sideways like this. My text will be much more extensive so the font won’t be able to be so big.
Nice to have
• The photo titled “sideways writing and silver rim” - I want 1C to be written sideways like this. My text will be much more extensive so the font won’t be able to be so big. I also REALLY like how this label is rimmed in silver, but I would want gold. This is not mandatory, but I really like this.
• The photo titled “melted honey” - This is another option I really like. The gold that looks like honey dripping on the label is really cool. Not mandatory, but I really liked that. I also like the craft background on this.
• Color Inspiration - The photo titled “color inspiration” and “another color inspiration” is an option I would also like to see. Rather than black, I’d like to see what it would ALSO look like with a navy background. NAVY, GOLD, WHITE, maybe black somewhere.
Should not have
• Colorful patterns or excessive info in section 1B.

```html
<!DOCTYPE html>
<html lang="en">
<head>
<meta charset="UTF-8">
<title>Clear Skin Body Polish – Label</title>
<link href="https://fonts.googleapis.com/css2?family=Jost:wght@300;400;500&display=swap" rel="stylesheet">
<style>
  :root {
    --page-bg: #f4f4f4;
    --label-edge: #a8a8a8;
    --label-mid: #dcdcdc;
    --label-light: #f5f5f5;
    --band-white: #ededed;
    --ink-grey: #585858;
    --ink-soft: #7a7a7a;
    --gold-dark: #8f610a;
    --gold: #c58b1a;
    --gold-light: #ecd08a;
    --white: #ffffff;
  }
  * { box-sizing: border-box; margin: 0; padding: 0; }
  html, body {
    width: 1200px;
    height: 1200px;
    overflow: hidden;
    background: var(--page-bg);
    font-family: "Jost", sans-serif;
  }
  .label {
    position: absolute;
    left: 100px;
    top: 195px;
    width: 1000px;
    height: 810px;
    background: linear-gradient(90deg, var(--label-edge) 0%, var(--label-mid) 14%, var(--label-light) 40%, var(--label-mid) 66%, var(--label-edge) 100%);
    overflow: hidden;
  }
  .logo-art {
    position: absolute;
    left: 47px;
    top: 180px;
    width: 560px;
    height: 506px;
    border-radius: 60px 60px 0 0;
    background: linear-gradient(135deg, var(--gold-dark) 0%, var(--gold) 30%, var(--gold-light) 55%, var(--gold) 80%, var(--gold-dark) 100%);
  }
  .product-title {
    position: absolute;
    right: 339px;
    top: 44px;
    text-align: right;
    color: var(--ink-grey);
    font-weight: 400;
    line-height: 1;
  }
  .product-title .line-top { font-size: 66px; display: block; }
  .product-title .line-bottom { font-size: 76px; display: block; margin-top: 2px; }
  .brand-band {
    position: absolute;
    left: 707px;
    top: 0;
    width: 160px;
    height: 686px;
    background: linear-gradient(90deg, var(--white) 0%, var(--band-white) 100%);
    border-left: 2px solid #d4d4d4;
    border-right: 2px solid #cecece;
  }
  .brand-name {
    position: absolute;
    left: 50%;
    top: 352px;
    transform: translate(-50%, -50%) rotate(-90deg);
    white-space: nowrap;
    font-size: 100px;
    font-weight: 300;
    color: var(--ink-soft);
  }
  .weight-band {
    position: absolute;
    left: 0;
    top: 686px;
    width: 100%;
    height: 70px;
    background: linear-gradient(90deg, var(--gold-dark) 0%, var(--gold) 8%, var(--gold-light) 32%, var(--gold) 58%, var(--gold-light) 78%, var(--gold-dark) 100%);
    display: flex;
    align-items: center;
    justify-content: center;
    color: var(--white);
    font-size: 34px;
    font-weight: 400;
    letter-spacing: 1px;
    padding-left: 40px;
  }
  .weight-band .divider { margin: 0 18px; }
  .label-foot {
    position: absolute;
    left: 0;
    bottom: 0;
    width: 100%;
    height: 54px;
    background: linear-gradient(90deg, #cdcdcd 0%, var(--label-light) 40%, var(--label-light) 70%, #cdcdcd 100%);
  }
</style>
</head>
<body>
  <section class="label">
    <div class="logo-art" role="img" aria-label="Golden elephant logo with raised trunk"></div>
    <h1 class="product-title">
      <span class="line-top">Clear Skin</span>
      <span class="line-bottom">Body Polish</span>
    </h1>
    <div class="brand-band">
      <div class="brand-name">BRAND NAME</div>
    </div>
    <div class="weight-band">
      <span>12 oz</span><span class="divider">|</span><span>340g</span>
    </div>
    <div class="label-foot"></div>
  </section>
</body>
</html>
```